Modern Label for cleaning products for the brand Voralux

We need a label design for our line of cleaning products. The label should feature our logo and an image to identify the product's intended use. I've added our logo and an image for use. This only concerns the design of the label on the front of the bottle.

Label dimensions:
Label 1 (500ml bottle with spray): width 58mm x height 115mm
Label 2: (1L bottle): width 73mm x height 140mm
The design must be consistent for both bottles which you find in the pictures.

The bottles to be labeled are white. See the attachment for a photo of the bottles.

The photo must also appear on the label to identify the product's intended use.

Product information:
Brand: Voralux
Product: Sanitary Cleaner

This text must be placed on the label:
"Cleans, descales & freshens. followed with this text: "Ideal for quick and powerful cleaning. A ready-to-use product for everyday use."

- Mention the seperate USP's: Sanitary, Bathroom, Toilet, Wet areas

Appearance: This is a consumer product, but it must have a professional appearance. We would like to see a design that use the color blue from our logo.

Target Market(s)

Consumers who take care of their homes and want to maintain it the correct (professional) way

Font styles to use
Sans Serif

Colors
0054AA
0677BA
7BADD7
CADEEF
E8F1F8

Requirements
Must have
• USP's + use of image and logo + blend in 1 design
Nice to have
• Keep the color of the logo in the design
Should not have
• Comic sans

```html
<!DOCTYPE html>
<html lang="en">
<head>
<meta charset="utf-8">
<title>Voralux Sanitary Cleaner – Label Set</title>
<link href="https://fonts.googleapis.com/css2?family=Arimo&family=Baloo+2:wght@800&family=Fjalla+One&family=Montserrat:wght@400;600&family=Poppins:wght@600&display=swap" rel="stylesheet">
<style>
  :root{
    --brand-deep:#0054AA;
    --brand-blue:#0677BA;
    --brand-sky:#7BADD7;
    --brand-mist:#CADEEF;
    --brand-ice:#E8F1F8;
    --label-bottom:#a3d6f5;
    --ink:#1d1d1b;
    --dim-blue:#2f6da6;
    --bg-center:#fbfcf2;
    --bg-edge:#dbe78f;
  }
  *{margin:0;padding:0;box-sizing:border-box}
  html,body{width:1200px;height:1200px;overflow:hidden}
  body{
    position:relative;
    background:radial-gradient(circle at 50% 50%,var(--bg-center) 0%,#eef4cc 45%,var(--bg-edge) 100%);
    font-family:"Montserrat",sans-serif;
  }
  .brand-lockup{position:absolute;left:217px;top:136px;width:250px;text-align:center}
  .brand-dot{display:block;margin:0 auto;width:100px;height:100px;border-radius:50%;background:var(--brand-blue)}
  .brand-name{font-family:"Poppins",sans-serif;font-weight:600;color:var(--ink);font-size:52px;line-height:1;margin-top:8px;letter-spacing:0.5px}

  .dimensions{position:absolute;left:0;top:0}
  .dimensions text{font-family:"Arimo",sans-serif;fill:var(--dim-blue)}

  .label{position:absolute;background:linear-gradient(to bottom,#ffffff 0%,var(--brand-ice) 25%,#cbe8fa 60%,var(--label-bottom) 100%);overflow:hidden}
  .label > *{position:absolute;left:0;width:100%;text-align:center}
  .label-small{left:193px;top:495px;width:302px;height:600px}
  .label-large{left:673px;top:365px;width:381px;height:730px}

  .label .mark{border-radius:50%;background:var(--brand-blue)}
  .label .wordmark{font-family:"Poppins",sans-serif;font-weight:600;color:var(--ink);line-height:1}
  .product-title{font-family:"Baloo 2",sans-serif;font-weight:800;color:var(--brand-blue);line-height:1;text-shadow:3px 3px 0 #111;letter-spacing:0.5px}
  .claim{font-family:"Fjalla One",sans-serif;color:var(--brand-blue);line-height:1;letter-spacing:0.2px}
  .intro{color:var(--brand-blue);line-height:1.25}
  .usage-photo{background:linear-gradient(135deg,#8d8d8d 0%,#b9b9b9 30%,#f1f1f1 55%,#e4e4e4 75%,#9a9a9a 100%)}
  .seal{border-radius:50%;background:var(--brand-blue);border:3px solid #fff;box-shadow:0 0 0 2px var(--brand-blue)}
  .usp-list{font-family:"Montserrat",sans-serif;font-weight:600;color:var(--brand-deep);line-height:1;letter-spacing:0.3px}
  .statement{color:#222;line-height:1.2}
  .volume{color:var(--brand-blue);line-height:1}

  /* small label */
  .label-small .mark{left:129px;top:26px;width:50px;height:50px}
  .label-small .wordmark{top:83px;font-size:22px}
  .label-small .title-1{top:123px;font-size:60px}
  .label-small .title-2{top:176px;font-size:60px}
  .label-small .claim{top:247px;font-size:19px}
  .label-small .intro{top:271px;font-size:11px}
  .label-small .usage-photo{left:42px;top:327px;width:218px;height:138px}
  .label-small .seal{left:199px;top:320px;width:72px;height:72px}
  .label-small .usp-list{top:474px;font-size:9.5px}
  .label-small .statement{top:497px;font-size:12.5px}
  .label-small .volume{top:561px;font-size:23px}

  /* large label */
  .label-large .mark{left:159px;top:21px;width:62px;height:62px}
  .label-large .wordmark{top:89px;font-size:29px}
  .label-large .title-1{top:141px;font-size:74px}
  .label-large .title-2{top:203px;font-size:74px}
  .label-large .claim{top:293px;font-size:24px}
  .label-large .intro{top:321px;font-size:13.5px}
  .label-large .usage-photo{left:55px;top:391px;width:269px;height:169px}
  .label-large .seal{left:249px;top:381px;width:90px;height:90px}
  .label-large .usp-list{top:573px;font-size:12px}
  .label-large .statement{top:599px;font-size:15.5px}
  .label-large .volume{top:692px;font-size:23px}
</style>
</head>
<body>

<div class="brand-lockup">
  <span class="brand-dot"></span>
  <div class="brand-name">Voralux</div>
</div>

<svg class="dimensions" width="1200" height="1200" viewBox="0 0 1200 1200" aria-hidden="true">
  <defs>
    <marker id="arrow" viewBox="0 0 10 10" refX="10" refY="5" markerWidth="12" markerHeight="8" orient="auto-start-reverse" markerUnits="userSpaceOnUse">
      <path d="M0 0 L10 5 L0 10 Z" fill="#2f6da6"/>
    </marker>
  </defs>
  <g stroke="#2f6da6" stroke-width="1.2" fill="none">
    <line x1="193" y1="454" x2="193" y2="484"/>
    <line x1="494" y1="454" x2="494" y2="484"/>
    <line x1="194" y1="466" x2="262" y2="466" marker-start="url(#arrow)"/>
    <line x1="427" y1="466" x2="493" y2="466" marker-end="url(#arrow)"/>
    <line x1="147" y1="495" x2="187" y2="495"/>
    <line x1="147" y1="1094" x2="187" y2="1094"/>
    <line x1="160" y1="496" x2="160" y2="700" marker-start="url(#arrow)"/>
    <line x1="160" y1="880" x2="160" y2="1093" marker-end="url(#arrow)"/>
    <line x1="673" y1="322" x2="673" y2="354"/>
    <line x1="1053" y1="322" x2="1053" y2="354"/>
    <line x1="674" y1="336" x2="782" y2="336" marker-start="url(#arrow)"/>
    <line x1="946" y1="336" x2="1052" y2="336" marker-end="url(#arrow)"/>
    <line x1="620" y1="365" x2="660" y2="365"/>
    <line x1="620" y1="1094" x2="660" y2="1094"/>
    <line x1="633" y1="366" x2="633" y2="635" marker-start="url(#arrow)"/>
    <line x1="633" y1="818" x2="633" y2="1093" marker-end="url(#arrow)"/>
  </g>
  <text x="344" y="478" font-size="34" text-anchor="middle">58.00 mm</text>
  <text x="864" y="348" font-size="34" text-anchor="middle">73.00 mm</text>
  <text transform="translate(172 790) rotate(-90)" font-size="34" text-anchor="middle">115.00 mm</text>
  <text transform="translate(645 727) rotate(-90)" font-size="34" text-anchor="middle">140.00 mm</text>
</svg>

<section class="label label-small" aria-label="Label for 500ml spray bottle">
  <span class="mark"></span>
  <div class="wordmark">Voralux</div>
  <h1 class="product-title title-1">Sanitary</h1>
  <div class="product-title title-2">Cleaner</div>
  <p class="claim">Cleans, Descales &amp; Freshens</p>
  <p class="intro">Ideal for quick and powerful cleaning.<br>A ready-to-use product for everyday use</p>
  <div class="usage-photo" role="img" aria-label="Photo of a modern grey-tiled bathroom with glass shower, washbasin and bathtub"></div>
  <div class="seal" role="img" aria-label="Certified organic seal"></div>
  <p class="usp-list">Sanitary · Bathroom · Toilet · Wet areas</p>
  <p class="statement">We use 100% certified organic cleaners,<br>ensuring a safe working environment free<br>of harmful chemicals.</p>
  <p class="volume">500ml</p>
</section>

<section class="label label-large" aria-label="Label for 1 litre bottle">
  <span class="mark"></span>
  <div class="wordmark">Voralux</div>
  <h2 class="product-title title-1">Sanitary</h2>
  <div class="product-title title-2">Cleaner</div>
  <p class="claim">Cleans, Descales &amp; Freshens</p>
  <p class="intro">Ideal for quick and powerful cleaning.<br>A ready-to-use product for everyday use</p>
  <div class="usage-photo" role="img" aria-label="Photo of a modern grey-tiled bathroom with glass shower, washbasin and bathtub"></div>
  <div class="seal" role="img" aria-label="Certified organic seal"></div>
  <p class="usp-list">Sanitary · Bathroom · Toilet · Wet areas</p>
  <p class="statement">We use 100% certified organic cleaners,<br>ensuring a safe working environment free<br>of harmful chemicals.</p>
  <p class="volume">1.000ml</p>
</section>

</body>
</html>
```